Business Card Design

We are a General Practice - Family medicine
We also have Allied Health professionals working within our team

Industry/Entity Type

Business

Contact Information for Business Card

Front of the card to display:

BRAMBLEWICK MEDICAL
PHONE 6348 2917

5/41 Fennimore Parade
Launceston Tasmania 7284

Back of the card to display:

My Appointments
Date:
Time:
With:

Please remember to phone us on 6348 2917 to cancel your appointment if you can't keep it.
A fee applied to missed appointments

```html
<!DOCTYPE html>
<html lang="en">
<head>
<meta charset="utf-8">
<title>Bramblewick Medical – Business Card</title>
<link rel="stylesheet" href="https://fonts.googleapis.com/css2?family=PT+Sans:wght@400;700&family=Questrial&display=swap">
<style>
  :root {
    --backdrop: #8c8d8f;
    --card-white: #ffffff;
    --sky-deep: #3fa3dd;
    --sky-mid: #8cc8ec;
    --sky-pale: #e9f5fc;
    --leaf-green: #8cc63f;
    --brand-blue: #3a9ad9;
    --ink-dark: #2f3236;
    --ink-grey: #55585c;
    --rule-grey: #6d7074;
  }
  * { box-sizing: border-box; margin: 0; padding: 0; }
  html, body { width: 1200px; height: 743px; overflow: hidden; }
  body {
    background: var(--backdrop);
    position: relative;
    font-family: "PT Sans", sans-serif;
  }
  .card {
    position: absolute;
    top: 221px;
    width: 520px;
    height: 300px;
    background: var(--card-white);
    overflow: hidden;
    box-shadow: 0 6px 18px rgba(0,0,0,0.25);
  }
  .card-front { left: 50px; }
  .card-back { left: 630px; }
  .card-art { position: absolute; inset: 0; width: 100%; height: 100%; }

  /* Front */
  .brand {
    position: absolute;
    right: 34px;
    top: 42px;
    text-align: right;
  }
  .brand-row { display: flex; align-items: center; justify-content: flex-end; gap: 10px; }
  .brand-dot {
    width: 18px; height: 18px; border-radius: 50%;
    background: var(--leaf-green);
  }
  .brand-name {
    font-family: "PT Sans", sans-serif;
    font-weight: 400;
    font-size: 34px;
    color: var(--brand-blue);
    letter-spacing: 0.5px;
  }
  .brand-descriptor {
    margin-top: 2px;
    font-family: "PT Sans", sans-serif;
    font-size: 13px;
    letter-spacing: 5px;
    color: var(--ink-grey);
  }
  .contact {
    position: absolute;
    left: 38px;
    top: 148px;
    color: var(--ink-dark);
    font-size: 19px;
    line-height: 1.3;
  }
  .contact-line { display: flex; align-items: flex-start; gap: 8px; }
  .contact-line + .contact-line { margin-top: 8px; }
  .contact-icon { width: 16px; height: 20px; flex: none; margin-top: 2px; }

  /* Back */
  .appointments {
    position: absolute;
    left: 40px;
    top: 26px;
    width: 440px;
    font-family: "Questrial", sans-serif;
  }
  .appointments-title {
    color: var(--brand-blue);
    font-size: 17px;
    font-weight: 700;
    font-family: "PT Sans", sans-serif;
    margin-left: 26px;
    margin-bottom: 14px;
  }
  .appointment-field {
    display: flex;
    align-items: flex-end;
    gap: 8px;
    height: 32px;
    color: var(--ink-grey);
    font-size: 17px;
  }
  .appointment-field .field-label { width: 48px; text-align: right; }
  .appointment-field .field-rule {
    flex: 1;
    border-bottom: 1px solid var(--rule-grey);
    margin-bottom: 4px;
    margin-right: 30px;
  }
  .reminder {
    position: absolute;
    left: 0; right: 0;
    top: 208px;
    text-align: center;
    font-family: "Questrial", sans-serif;
    color: var(--ink-grey);
    font-size: 15.5px;
    line-height: 1.3;
  }
  .reminder-fee { margin-top: 8px; }
</style>
</head>
<body>

  <section class="card card-front" aria-label="Card front">
    <svg class="card-art" viewBox="0 0 520 300" aria-hidden="true">
      <defs>
        <linearGradient id="frontSky" x1="0" y1="0" x2="1" y2="1">
          <stop offset="0" stop-color="var(--sky-mid)"/>
          <stop offset="0.45" stop-color="var(--sky-pale)"/>
          <stop offset="1" stop-color="var(--sky-deep)"/>
        </linearGradient>
      </defs>
      <path d="M0,80 C170,60 320,170 520,252 L520,300 L0,300 Z" fill="url(#frontSky)"/>
      <path d="M0,72 C170,52 320,162 520,244 L520,249 C320,168 170,58 0,77 Z" fill="var(--sky-mid)"/>
      <path d="M320,190 C400,232 460,252 520,258 L520,268 C450,262 385,238 320,190 Z" fill="var(--leaf-green)"/>
    </svg>

    <div class="brand">
      <div class="brand-row">
        <span class="brand-dot"></span>
        <span class="brand-name">Bramblewick Medical</span>
      </div>
      <div class="brand-descriptor">HEALTHCARE CENTRE</div>
    </div>

    <div class="contact">
      <div class="contact-line">
        <svg class="contact-icon" viewBox="0 0 16 20" aria-hidden="true">
          <path d="M4,2 L7,2 L8,7 L6,8.5 C7,11 8.5,13 11,14 L12.5,12 L15,13.5 L14,17 C8,17 3,11 3,4 Z" fill="var(--brand-blue)"/>
        </svg>
        <span>6348 2917</span>
      </div>
      <div class="contact-line">
        <svg class="contact-icon" viewBox="0 0 16 20" aria-hidden="true">
          <path d="M8,1 C4,1 1.5,4 1.5,7.5 C1.5,12 8,19 8,19 C8,19 14.5,12 14.5,7.5 C14.5,4 12,1 8,1 Z M8,5 A2.6,2.6 0 1 1 7.99,5 Z" fill="var(--brand-blue)" fill-rule="evenodd"/>
        </svg>
        <span>5/41 Fennimore Parade<br>Launceston Tasmania 7284</span>
      </div>
    </div>
  </section>

  <section class="card card-back" aria-label="Card back">
    <svg class="card-art" viewBox="0 0 520 300" aria-hidden="true">
      <defs>
        <linearGradient id="backSky" x1="0" y1="0" x2="1" y2="1">
          <stop offset="0" stop-color="var(--sky-deep)"/>
          <stop offset="0.5" stop-color="var(--sky-pale)"/>
          <stop offset="1" stop-color="var(--sky-mid)"/>
        </linearGradient>
      </defs>
      <path d="M0,200 C150,194 330,190 520,186 L520,300 L0,300 Z" fill="url(#backSky)"/>
      <path d="M0,168 C60,186 140,190 260,188 C140,196 60,194 0,182 Z" fill="var(--leaf-green)"/>
    </svg>

    <div class="appointments">
      <h2 class="appointments-title">My appointments:</h2>
      <div class="appointment-field"><span class="field-label">Date</span><span class="field-rule"></span></div>
      <div class="appointment-field"><span class="field-label">Time</span><span class="field-rule"></span></div>
      <div class="appointment-field"><span class="field-label">With</span><span class="field-rule"></span></div>
    </div>

    <div class="reminder">
      <p>Please remember to phone us on 6348 2917 to cancel<br>your appointment if you can't keep it.</p>
      <p class="reminder-fee">A fee applied to missed appointments.</p>
    </div>
  </section>

</body>
</html>
```